Software allocation system needs a business card design

We need a business card designed for our software platform - www.tolvexa.com.au

At the moment the logo and website is all black and white, we are happy for suggestions on implementing some colour throughout either the logo or business card.

Industry/Entity Type

Software

Font styles to use
Sans Serif

Colors

Designer to choose colors to be used in the design.

```html
<!DOCTYPE html>
<html lang="en">
<head>
<meta charset="utf-8">
<title>Tolvexa — Business Card</title>
<link rel="stylesheet" href="https://fonts.googleapis.com/css2?family=Mulish:wght@400;700;800&display=swap">
<style>
  :root {
    --backdrop: #2a2a2c;
    --card-white: #ffffff;
    --brand-blue: #0b5fae;
    --deep-blue: #0a2f7a;
    --bright-blue: #1a7fe0;
    --text-dark: #3a3a3a;
    --link-blue: #1b6cc0;
  }
  html, body {
    margin: 0;
    width: 1200px;
    height: 1000px;
    overflow: hidden;
    background: var(--backdrop);
    font-family: "Mulish", sans-serif;
  }
  .canvas {
    width: 1200px;
    height: 1000px;
    display: flex;
    align-items: center;
    justify-content: center;
  }
  .card {
    position: relative;
    width: 900px;
    height: 520px;
    background: var(--card-white);
    border-radius: 18px;
    overflow: hidden;
    box-shadow: 0 20px 50px rgba(0,0,0,0.45);
  }
  .card__visual {
    position: absolute;
    left: 0; top: 0;
    width: 380px;
    height: 100%;
    background: linear-gradient(135deg, var(--deep-blue) 0%, var(--brand-blue) 55%, var(--bright-blue) 100%);
  }
  .card__logo-band {
    position: absolute;
    left: 300px;
    top: 62px;
    width: 640px;
    height: 150px;
    background: var(--card-white);
    border-radius: 75px 0 0 75px;
  }
  .brand {
    position: absolute;
    left: 360px;
    top: 100px;
    display: flex;
    align-items: center;
    gap: 18px;
  }
  .brand__dot {
    width: 40px; height: 40px;
    border-radius: 50%;
    background: var(--brand-blue);
  }
  .brand__name {
    font-size: 68px;
    font-weight: 400;
    letter-spacing: 6px;
    color: var(--brand-blue);
    line-height: 1;
  }
  .holder {
    position: absolute;
    left: 60px;
    top: 250px;
    color: #fff;
  }
  .holder__name {
    font-size: 32px;
    font-weight: 800;
    margin: 0;
  }
  .holder__role {
    font-size: 24px;
    margin: 2px 0 0;
  }
  .contact {
    position: absolute;
    left: 440px;
    top: 282px;
    color: var(--text-dark);
    font-size: 22px;
    line-height: 1.35;
  }
  .contact p { margin: 0; }
  .contact__phone { font-weight: 700; }
  .contact__address { margin-top: 22px !important; }
  .contact__web { color: var(--link-blue); }
</style>
</head>
<body>
  <main class="canvas">
    <section class="card">
      <div class="card__visual" role="img" aria-label="Blue-toned photograph area"></div>
      <div class="card__logo-band"></div>
      <div class="brand">
        <span class="brand__dot"></span>
        <span class="brand__name">TOLVEXA</span>
      </div>
      <div class="holder">
        <p class="holder__name">Daniel Corwin</p>
        <p class="holder__role">CEO</p>
      </div>
      <div class="contact">
        <p class="contact__phone">+01 79 555 12 34</p>
        <p>hello@tolvexa.com.au</p>
        <p class="contact__address">PO Box 218</p>
        <p>Fernhill NSW 2260</p>
        <p class="contact__web">www.tolvexa.com.au</p>
      </div>
    </section>
  </main>
</body>
</html>
```